Detox Poster Design Project

I am a naturopath that works in Melbourne. I require a poster that I can put up in my natural therapies clinic that is advertising a detox program that I am offering. The program runs for 3 or 6 weeks and is designed to help your liver, gut and kidney cleanse toxins more efficiently, leaving you feeling energised and healthy.

I would like to see designs that are fresh, organic, clear and contemporary to look at. I want to sell the idea of feeling good, wellbeing and vitality to the potential client. Colours I like include greens, greys and blues.

The final design should communicate health and happiness.

• Please include the photo of the woman in nature.Poster size will be A2 594mm by 420mm
• I have attached the design work for my business cards that you can use. It would be great if the colours and style are in keeping with the existing design work for my business. I have also attached an extra image (almond milk photo) just in case you could see a use for it.

Many thanks.
• No hippy, new age looking design.

```html
<!DOCTYPE html>
<html lang="en">
<head>
<meta charset="utf-8">
<title>It's Sensible Detox Time!</title>
<link rel="stylesheet" href="https://fonts.googleapis.com/css2?family=Fredoka:wght@500;600&family=Quicksand:wght@500;700&display=swap">
<style>
  :root {
    --frame-green: #4b8a3e;
    --leaf-deep: #1f3d16;
    --leaf-dark: #2f5a22;
    --leaf-mid: #5f9a3c;
    --leaf-bright: #8cc04a;
    --leaf-light: #cfe58a;
    --sun-glow: #eef6c4;
    --soft-light: #e8ece2;
    --panel-grey: #efefef;
    --accent-blue: #14a6d3;
    --ink: #3a3a3a;
  }
  * { margin: 0; padding: 0; box-sizing: border-box; }
  html, body { width: 848px; height: 1200px; overflow: hidden; background: #ffffff; }
  .poster {
    position: relative;
    width: 848px;
    height: 1200px;
    background: var(--panel-grey);
    border: 8px solid var(--frame-green);
    overflow: hidden;
  }
  .hero-photo {
    position: absolute;
    left: 0; top: 0;
    width: 832px; height: 800px;
    background:
      radial-gradient(ellipse 30% 22% at 88% 18%, var(--sun-glow) 0%, rgba(238,246,196,0) 100%),
      radial-gradient(ellipse 34% 40% at 80% 30%, var(--leaf-light) 0%, rgba(207,229,138,0) 100%),
      radial-gradient(ellipse 16% 50% at 52% 62%, var(--soft-light) 0%, rgba(232,236,226,0) 100%),
      radial-gradient(ellipse 30% 25% at 12% 82%, var(--leaf-bright) 0%, rgba(140,192,74,0) 100%),
      radial-gradient(ellipse 40% 35% at 20% 20%, var(--leaf-deep) 0%, rgba(31,61,22,0) 100%),
      radial-gradient(ellipse 35% 30% at 85% 75%, var(--leaf-dark) 0%, rgba(47,90,34,0) 100%),
      radial-gradient(ellipse 20% 15% at 35% 45%, var(--leaf-bright) 0%, rgba(140,192,74,0) 100%),
      linear-gradient(165deg, var(--leaf-dark) 0%, var(--leaf-mid) 50%, var(--leaf-dark) 100%);
  }
  .swoosh {
    position: absolute;
    left: 0; top: 700px;
    width: 832px; height: 200px;
  }
  .headline {
    position: absolute;
    left: 0; top: 812px;
    width: 832px;
    text-align: center;
    font-family: "Fredoka", sans-serif;
    font-weight: 600;
    font-size: 71px;
    line-height: 90px;
    letter-spacing: 0;
    white-space: nowrap;
    color: var(--accent-blue);
    transform: rotate(-0.8deg);
  }
  .pitch {
    position: absolute;
    left: 0; top: 914px;
    width: 832px;
    text-align: center;
    font-family: "Quicksand", sans-serif;
    font-weight: 500;
    font-size: 24.5px;
    color: var(--ink);
  }
  .pitch p { line-height: 45.5px; white-space: nowrap; }
  .pitch strong { color: var(--accent-blue); font-weight: 700; }
  .contact {
    position: absolute;
    left: 40px; top: 1077px;
    font-family: "Quicksand", sans-serif;
    font-style: normal;
    font-weight: 500;
    font-size: 22px;
    line-height: 25px;
    color: var(--ink);
  }
  .contact .contact-name { color: var(--accent-blue); font-weight: 700; }
</style>
</head>
<body>
  <main class="poster">
    <div class="hero-photo" role="img" aria-label="Woman seen from behind with arms raised in a lush green tropical garden"></div>

    <svg class="swoosh" viewBox="0 0 832 200" aria-hidden="true">
      <path d="M0 46 Q 400 110 832 30 L832 200 L0 200 Z" fill="var(--frame-green)"/>
      <path d="M0 86 Q 400 130 832 74 L832 200 L0 200 Z" fill="var(--panel-grey)"/>
    </svg>

    <h1 class="headline">It’s Sensible Detox Time!</h1>

    <section class="pitch">
      <p><strong>Overindulge</strong> over the holidays?</p>
      <p>Have a <strong>detox program</strong> tailored for you.</p>
      <p>Press <strong>reset</strong> on your bad eating habits to feel <strong>energised</strong> and <strong>vital</strong>.</p>
    </section>

    <address class="contact">
      <div>For more information:</div>
      <div class="contact-name">Clara Whitfield</div>
      <div>0400 123 456</div>
      <div>hello@greenleafwellness.com</div>
    </address>
  </main>
</body>
</html>
```